Business Card For Video Production Company

Please NOTE: I've added some info to the must haves that I should have included at the start. Thank you.

I need a business card design for my video production company based in Orlando called Halvard Lens Productions. Our work consists of web video marketing (web videos), training videos, sales videos, conference and seminar video production...basically a lot of corporate based work.

We work with successful small businesses, not-for-profits and some Summit 700 type groups. We bring a lot of knowledge, experience and attention to detail to every project.

I'd like something that communicates strength, confidence, integrity, as well as creative vision. I want to stay away from the standard icons of the media and film industry. I'd like to emphasize the colors of my logo, and also the colors of my website which has a white background. Simple is good.

Our budgets are moderate...generally $1500 to $5000.

www.halvardlens.tv

PS...We don't do weddings or recitals, or that type of production.
Updates

I want to thank all the designers for your updates. There's way too many to be able to give feedback on for all. I hope you understand that. But wow…there are so many great designs everyone has offered. I can't thank you enough…each and everyone. I hope to make my decision soon. I'm not accepting anymore designs from new designers. Dean-

Target Market(s)

Successful small businesses, marketing directors, corporate communication directors, training and human resources professionals. forward thinking not-for profits. Since my company is based in Central Florida, most of my work comes from this area too.

Industry/Entity Type

Marketing

Requirements
Must have
• website address, www.halvardlens.tv
phone number, 407-555-2937
email address, dean@halvardlens.tv

Title
Dean Halvard
Owner/Creative Director

I'd like to have a single line that goes across illustrating our services, maybe separated with bullet points:

Marketing Videos, Corporate Videos, Conference & Seminar Video Production
Should not have
• No film or video icons.
No need to pull language or copy from my website.

```html
<!DOCTYPE html>
<html lang="en">
<head>
<meta charset="utf-8">
<title>Halvard Lens Productions – Business Card</title>
<link href="https://fonts.googleapis.com/css2?family=PT+Sans:wght@400;700&display=swap" rel="stylesheet">
<style>
  :root {
    --page: #ffffff;
    --card-dark: #333333;
    --slate: #36414a;
    --slate-grey: #444a4c;
    --panel-blue: #2a7f9c;
    --accent-blue: #1a8fd6;
    --name-yellow: #f5d60f;
    --text-light: #ffffff;
    --tab-white: #eeeeee;
    --icon-dark: #333333;
  }
  * { margin: 0; padding: 0; box-sizing: border-box; }
  html, body {
    width: 1200px; height: 1000px; overflow: hidden;
    background: var(--page);
    font-family: "PT Sans", Arial, sans-serif;
  }
  .sheet { position: relative; width: 1200px; height: 1000px; }

  .card {
    position: absolute; left: 250px;
    width: 700px; height: 400px;
    background: var(--card-dark);
    overflow: hidden;
  }
  .card--front { top: 50px; }
  .card--back { top: 530px; }

  /* Soft tonal backdrop standing in for the large decorative emblem */
  .backdrop {
    position: absolute;
  }
  .card--front .backdrop {
    left: 0; top: 0; width: 520px; height: 400px;
    background: linear-gradient(160deg, var(--slate) 0%, var(--slate) 35%, var(--slate-grey) 70%, rgba(68,74,76,0) 100%);
  }
  .card--back .backdrop {
    left: 80px; top: 0; width: 500px; height: 400px;
    background: linear-gradient(180deg, var(--slate) 0%, var(--slate-grey) 60%, var(--slate-grey) 100%);
    opacity: 0.95;
  }

  /* Front face */
  .brand {
    position: absolute; left: 0; right: 0; top: 0; bottom: 0;
    display: flex; align-items: center; justify-content: center; gap: 16px;
  }
  .brand__mark { width: 34px; height: 34px; background: var(--accent-blue); }
  .brand__name {
    color: var(--text-light); font-weight: 700; font-size: 34px; letter-spacing: 0.5px;
  }

  /* Back face */
  .contact-panel {
    position: absolute; left: 408px; top: 42px; width: 292px; height: 326px;
    background: var(--panel-blue);
  }
  .contact-row {
    position: absolute; left: 400px; width: 300px; height: 52px;
    display: flex; align-items: center;
  }
  .contact-row--email { top: 82px; }
  .contact-row--phone { top: 178px; }
  .contact-row--web { top: 274px; }
  .contact-row__tab {
    width: 66px; height: 52px; background: var(--tab-white); border-radius: 6px;
    display: flex; align-items: center; justify-content: center; flex-shrink: 0;
  }
  .contact-row__tab svg { width: 30px; height: 30px; }
  .contact-row__text {
    flex: 1; text-align: center; color: var(--text-light); font-size: 19px;
  }

  .person { position: absolute; left: 34px; top: 314px; }
  .person__name {
    color: var(--name-yellow); font-size: 42px; font-weight: 700; letter-spacing: -1px; line-height: 1;
  }
  .person__title { color: var(--text-light); font-size: 20px; margin-top: 6px; }
</style>
</head>
<body>
<main class="sheet">

  <section class="card card--front" aria-label="Card front">
    <div class="backdrop" role="img" aria-label="Large faint slate-blue and grey brand emblem backdrop"></div>
    <div class="brand">
      <span class="brand__mark"></span>
      <span class="brand__name">Halvard Lens Productions</span>
    </div>
  </section>

  <section class="card card--back" aria-label="Card back">
    <div class="backdrop" role="img" aria-label="Large faint slate-blue and grey brand emblem backdrop"></div>
    <div class="contact-panel" role="img" aria-label="Blue panel with fine hexagon texture"></div>

    <div class="contact-row contact-row--email">
      <div class="contact-row__tab">
        <svg viewBox="0 0 30 30" aria-hidden="true">
          <rect x="6" y="7" width="18" height="12" rx="1" fill="none" stroke="var(--icon-dark)" stroke-width="2.4"/>
          <rect x="3" y="20" width="24" height="3" rx="1" fill="var(--icon-dark)"/>
        </svg>
      </div>
      <span class="contact-row__text">dean@halvardlens.tv</span>
    </div>

    <div class="contact-row contact-row--phone">
      <div class="contact-row__tab">
        <svg viewBox="0 0 30 30" aria-hidden="true">
          <path d="M9 4 L13 4 L14 10 L11.5 12 Q13 18 18 21.5 L20 19 L26 20 L26 24 Q25 27 21 26 Q8 22 5 9 Q5 5 9 4 Z" fill="var(--icon-dark)"/>
        </svg>
      </div>
      <span class="contact-row__text">407-555-2937</span>
    </div>

    <div class="contact-row contact-row--web">
      <div class="contact-row__tab">
        <svg viewBox="0 0 30 30" aria-hidden="true" fill="none" stroke="var(--icon-dark)" stroke-width="2">
          <circle cx="15" cy="15" r="11"/>
          <ellipse cx="15" cy="15" rx="5" ry="11"/>
          <line x1="4" y1="15" x2="26" y2="15"/>
          <line x1="6" y1="9" x2="24" y2="9"/>
          <line x1="6" y1="21" x2="24" y2="21"/>
        </svg>
      </div>
      <span class="contact-row__text">www.halvardlens.tv</span>
    </div>

    <div class="person">
      <div class="person__name">Dean Halvard</div>
      <div class="person__title">Owner/Creative Director</div>
    </div>
  </section>

</main>
</body>
</html>
```